Brochure design

I need a Homecare brochure designed I will be caring for elderly and people with disabilities in their own homes. Would like it trifold and able to put text on both sides

Target Market(s)

Elderly as well as children and adults with disabilities

Industry/Entity Type

Homecare

Font styles to use
Serif
Other font styles liked:
• Would like colors from my logo

Colors
A7469A
B969AE
D3A5CF
EDDBEB
F8F0F9

Requirements
Must have
• Non medical services we provide; Dementia / Alzheimer care, Respite care, Companionship, light housekeeping, errand services, escort to medical appointments, medication reminders, meal preparation, special needs children, youth, or adults, morning perk up’s, evening tuck ins|’s.
Nice to have
• Why choose Quiet Harbor Homecare : * caregivers are highly trained, screened and experienced * client to caregiver matching to ensure compatibility *Regular pop in’s by management to ensure client satisfaction *our level of service exceeds the industry standards *24 hour services including holidays and weekends* Flexible payment options. Contact your local QHH Homecare office for a free in home consultation and explore your options today.
Should not have
• No pictures of stethoscope’s as we are non medical. Please see pictures of my friends brochure as a guid to what needs to be on it. Let me know if you have questions

```html
<!DOCTYPE html>
<html lang="en">
<head>
<meta charset="UTF-8">
<title>Quiet Harbor Homecare – Trifold Brochure</title>
<link rel="stylesheet" href="https://fonts.googleapis.com/css2?family=Playfair+Display:wght@700;800&family=Lora:wght@400;500;600&display=swap">
<style>
:root{
  --plum:#A7469A;
  --orchid:#B969AE;
  --lilac:#D3A5CF;
  --mist:#EDDBEB;
  --blush:#F8F0F9;
  --ink:#3a3340;
  --soft-ink:#645c69;
  --stage:#ececee;
  --paper:#ffffff;
}
*{margin:0;padding:0;box-sizing:border-box}
html,body{width:673px;height:1200px;overflow:hidden}
body{background:var(--stage);font-family:"Lora",Georgia,serif;color:var(--ink);position:relative}

.side-label{position:absolute;left:20px;font-family:"Lora",Georgia,serif;font-size:9px;letter-spacing:1.5px;text-transform:uppercase;color:#8d8592}
.side-label--outside{top:100px}
.side-label--inside{top:600px}

.spread{position:absolute;left:20px;width:633px;height:450px;background:var(--paper);display:flex;box-shadow:0 6px 18px rgba(60,40,60,.15)}
.spread--outside{top:120px}
.spread--inside{top:620px}
.panel{position:relative;width:211px;height:100%;overflow:hidden}
.panel + .panel{border-left:1px dashed #e3dbe2}

.photo{position:absolute;background:linear-gradient(135deg,var(--lilac),var(--mist) 55%,#d6ccd0)}
.house{clip-path:polygon(0 26%,50% 0,100% 26%,100% 100%,0 100%)}
.band{position:absolute;left:0;right:0;bottom:0;background:var(--plum)}

.content{position:absolute;left:16px;right:16px}
.heading{font-family:"Playfair Display",Georgia,serif;font-weight:800;font-size:13px;line-height:1.2;color:var(--plum);text-transform:uppercase;letter-spacing:.2px}
.subhead{font-size:8px;font-weight:600;font-style:italic;color:var(--orchid);margin-top:3px}
.body-copy{font-size:7.2px;line-height:1.55;color:var(--soft-ink);margin-top:8px}
.ticks{list-style:none;margin-top:10px}
.ticks li{display:flex;gap:6px;align-items:flex-start;font-size:7.5px;line-height:1.4;margin-bottom:6px;color:var(--ink)}
.ticks svg{flex:none;width:9px;height:9px;margin-top:1px}

/* outside */
.why{top:24px}
.why-photo{left:0;right:0;bottom:24px;height:180px}
.why-band{height:24px}

.contact-backdrop{left:0;right:0;top:0;height:150px;background:linear-gradient(160deg,var(--blush),#f1e8ee 60%,var(--mist))}
.reach{top:170px}
.contact{list-style:none;margin-top:12px}
.contact li{display:flex;gap:6px;align-items:center;font-size:7.5px;color:var(--soft-ink);margin-bottom:7px}
.contact svg{width:9px;height:9px;flex:none}
.reach-band{height:24px}

.cover-backdrop{left:0;right:0;top:0;height:150px;background:linear-gradient(160deg,var(--blush),#efe6ec 60%,var(--mist))}
.brand{position:absolute;top:96px;left:50%;transform:translateX(-50%);display:flex;align-items:center;gap:6px;background:var(--paper);padding:8px 10px;white-space:nowrap}
.brand-mark{width:10px;height:10px;background:var(--plum)}
.brand-name{font-family:"Lora",Georgia,serif;font-size:10.5px;font-weight:600;color:var(--plum)}
.tagline{top:168px;text-align:center;font-size:14px}
.cover-photo{left:18px;right:18px;bottom:40px;height:190px;background:linear-gradient(135deg,var(--lilac),#d8cfd4 50%,var(--orchid))}
.cover-band{height:40px;background:linear-gradient(90deg,var(--plum),var(--orchid))}
.cover-note{position:absolute;left:0;right:0;bottom:14px;text-align:center;font-size:8px;font-style:italic;color:#fff}

/* inside */
.services{top:24px}
.services .ticks li{margin-bottom:5px}
.services-band{height:24px}

.stage-photo{left:0;right:0;top:24px;height:220px;background:linear-gradient(135deg,#d9c9c7,var(--mist) 45%,var(--lilac))}
.stage-text{top:262px}
.stage-band{height:24px}

.feature-photo{left:0;right:0;top:24px;height:220px;background:linear-gradient(150deg,var(--mist),#d8ccc4 55%,var(--lilac))}
.feature{top:262px}
.feature-band{height:24px}
</style>
</head>
<body>

<p class="side-label side-label--outside">Outside</p>
<section class="spread spread--outside">
  <div class="panel">
    <div class="content why">
      <h2 class="heading">Why choose<br>Quiet Harbor Homecare</h2>
      <ul class="ticks">
        <li><svg viewBox="0 0 10 10"><path d="M1 5.5l2.5 2.5L9 2" fill="none" stroke="var(--plum)" stroke-width="1.6"/></svg>Caregivers are highly trained, screened and experienced</li>
        <li><svg viewBox="0 0 10 10"><path d="M1 5.5l2.5 2.5L9 2" fill="none" stroke="var(--plum)" stroke-width="1.6"/></svg>Client to caregiver matching to ensure compatibility</li>
        <li><svg viewBox="0 0 10 10"><path d="M1 5.5l2.5 2.5L9 2" fill="none" stroke="var(--plum)" stroke-width="1.6"/></svg>Regular pop in’s by management to ensure client satisfaction</li>
        <li><svg viewBox="0 0 10 10"><path d="M1 5.5l2.5 2.5L9 2" fill="none" stroke="var(--plum)" stroke-width="1.6"/></svg>Our level of service exceeds the industry standards</li>
        <li><svg viewBox="0 0 10 10"><path d="M1 5.5l2.5 2.5L9 2" fill="none" stroke="var(--plum)" stroke-width="1.6"/></svg>24 hour services including holidays and weekends</li>
        <li><svg viewBox="0 0 10 10"><path d="M1 5.5l2.5 2.5L9 2" fill="none" stroke="var(--plum)" stroke-width="1.6"/></svg>Flexible payment options</li>
      </ul>
    </div>
    <div class="photo house why-photo" role="img" aria-label="Photo of a caregiver helping an elderly client at home"></div>
    <div class="band why-band"></div>
  </div>

  <div class="panel">
    <div class="photo contact-backdrop" role="img" aria-label="Faint photo of a bright home interior"></div>
    <div class="content reach">
      <h2 class="heading">Get in touch</h2>
      <p class="subhead">Free in home consultation</p>
      <p class="body-copy">Contact your local QHH Homecare office for a free in home consultation and explore your options today.</p>
      <ul class="contact">
        <li><svg viewBox="0 0 10 10"><path d="M2 1h2l1 2.5-1.3 1a5 5 0 0 0 2 2l1-1.3L9 6.2V8a1 1 0 0 1-1 1A7 7 0 0 1 1 2a1 1 0 0 1 1-1z" fill="var(--plum)"/></svg>(555) 014-2290</li>
        <li><svg viewBox="0 0 10 10"><path d="M5 1a3 3 0 0 1 3 3c0 2.2-3 5.5-3 5.5S2 6.2 2 4a3 3 0 0 1 3-3z" fill="var(--plum)"/><circle cx="5" cy="4" r="1" fill="#fff"/></svg>12 Harbor Lane, Suite 4</li>
        <li><svg viewBox="0 0 10 10"><circle cx="5" cy="5" r="4" fill="none" stroke="var(--plum)" stroke-width="1.2"/></svg>quietharborhomecare.example</li>
      </ul>
    </div>
    <div class="band reach-band"></div>
  </div>

  <div class="panel">
    <div class="photo cover-backdrop" role="img" aria-label="Faint photo of a caregiver with a client in a living room"></div>
    <div class="brand">
      <span class="brand-mark"></span>
      <span class="brand-name">Quiet Harbor Homecare</span>
    </div>
    <p class="content heading tagline">Remain in the comfort<br>of your own home.</p>
    <div class="photo house cover-photo" role="img" aria-label="Photo of a smiling caregiver with a senior client"></div>
    <div class="band cover-band"></div>
    <p class="cover-note">Caring for you where you live</p>
  </div>
</section>

<p class="side-label side-label--inside">Inside</p>
<section class="spread spread--inside">
  <div class="panel">
    <div class="content services">
      <h2 class="heading">Non medical services</h2>
      <p class="subhead">Care you can trust</p>
      <p class="body-copy">Our caring team supports seniors, children and adults with disabilities in the place they love most. Every plan is shaped around daily routines, comfort and dignity, so families enjoy peace of mind.</p>
      <ul class="ticks">
        <li><svg viewBox="0 0 10 10"><path d="M1 5.5l2.5 2.5L9 2" fill="none" stroke="var(--plum)" stroke-width="1.6"/></svg>Dementia / Alzheimer care</li>
        <li><svg viewBox="0 0 10 10"><path d="M1 5.5l2.5 2.5L9 2" fill="none" stroke="var(--plum)" stroke-width="1.6"/></svg>Respite care</li>
        <li><svg viewBox="0 0 10 10"><path d="M1 5.5l2.5 2.5L9 2" fill="none" stroke="var(--plum)" stroke-width="1.6"/></svg>Companionship</li>
        <li><svg viewBox="0 0 10 10"><path d="M1 5.5l2.5 2.5L9 2" fill="none" stroke="var(--plum)" stroke-width="1.6"/></svg>Light housekeeping</li>
        <li><svg viewBox="0 0 10 10"><path d="M1 5.5l2.5 2.5L9 2" fill="none" stroke="var(--plum)" stroke-width="1.6"/></svg>Errand services</li>
        <li><svg viewBox="0 0 10 10"><path d="M1 5.5l2.5 2.5L9 2" fill="none" stroke="var(--plum)" stroke-width="1.6"/></svg>Escort to medical appointments</li>
        <li><svg viewBox="0 0 10 10"><path d="M1 5.5l2.5 2.5L9 2" fill="none" stroke="var(--plum)" stroke-width="1.6"/></svg>Medication reminders</li>
        <li><svg viewBox="0 0 10 10"><path d="M1 5.5l2.5 2.5L9 2" fill="none" stroke="var(--plum)" stroke-width="1.6"/></svg>Meal preparation</li>
        <li><svg viewBox="0 0 10 10"><path d="M1 5.5l2.5 2.5L9 2" fill="none" stroke="var(--plum)" stroke-width="1.6"/></svg>Special needs children, youth or adults</li>
        <li><svg viewBox="0 0 10 10"><path d="M1 5.5l2.5 2.5L9 2" fill="none" stroke="var(--plum)" stroke-width="1.6"/></svg>Morning perk up’s &amp; evening tuck in’s</li>
      </ul>
    </div>
    <div class="band services-band"></div>
  </div>

  <div class="panel">
    <div class="photo house stage-photo" role="img" aria-label="Photo of a caregiver assisting a client in a wheelchair"></div>
    <div class="content stage-text">
      <h2 class="heading">Support at every stage</h2>
      <p class="body-copy">From a short friendly visit to full day support, we match each client with a caregiver who truly fits their needs and personality.</p>
    </div>
    <div class="band stage-band"></div>
  </div>

  <div class="panel">
    <div class="photo house feature-photo" role="img" aria-label="Photo of a caregiver walking with an elderly client at home"></div>
    <div class="content feature">
      <h2 class="heading">Outstanding home care services</h2>
      <p class="body-copy">Our team arrives on time, follows your care plan and keeps families informed with simple updates after every visit.</p>
    </div>
    <div class="band feature-band"></div>
  </div>
</section>

</body>
</html>
```